BrivoMatex. Lantern for the Steady Growth. Business card

Professional business card for BrivoMatex (Lantern for the Steady Growth)
My rationale: Strategy-> Execution-> Results-> Value that lead to the BrivoMatex name: We put the Lantern for the Steady Growth.
We deliver value to our customers helping them at defining a good strategy (cyan arrow). 90% of well formulated strategies fail due to poor execution so we also consider strategical execution very important (green arrow). Due to the execution we obtain the results (blue arrow). Finally, the results provide feedback to redefine strategy, and the new strategy has to be executed and new results obtained providing new feedback and on and on. It's like a wheel that finally, must create corporate value: value for shareholders, staholders, employees, providers...-

Target Market(s)

CEOs and steering comitees , invewrnent funds

Industry/Entity Type

Business Consultant

Contact Information for Business Card

Tommaso Ferlini
CEO & Founder
tommaso.ferlini@brivomatex.example
Mobile: +34 611.205.938
www.brivomatex.example

Colors

Designer to choose colors to be used in the design.

Requirements
Nice to have
• Nice to hace the words: Strategy, execution, results
• Nice to vave the claim: Lantern for the Steady Growth
• The three colors should be shown:
• cyan for STRATEGY
• green for EXECUTION
• blue for RESULTS
Should not have
• Complete black background

```html
<!DOCTYPE html>
<html lang="en">
<head>
<meta charset="utf-8">
<title>BrivoMatex — Business Card</title>
<link rel="stylesheet" href="https://fonts.googleapis.com/css2?family=Roboto:wght@400;700&display=swap">
<style>
  :root {
    --stage: #14233a;
    --card: #161719;
    --map: #1f2022;
    --brand-blue: #1a3fb0;
    --cyan: #12aeea;
    --text-light: #d6d8dc;
    --text-muted: #b9bcc2;
    --divider: #a9acb2;
  }
  * { margin: 0; padding: 0; box-sizing: border-box; }
  html, body {
    width: 1200px; height: 1200px; overflow: hidden;
    background: var(--stage);
    font-family: "Roboto", Arial, sans-serif;
  }
  .sheet {
    width: 1200px; height: 1200px;
    display: flex; flex-direction: column; align-items: center; justify-content: center;
    gap: 60px;
  }
  .card {
    position: relative;
    width: 900px; height: 500px;
    background: var(--card);
    overflow: hidden;
  }

  /* Front */
  .front__map {
    position: absolute; left: 150px; top: 40px; width: 660px; height: 420px;
    border-radius: 40% 45% 38% 50%;
    background: radial-gradient(ellipse at center, var(--map) 55%, rgba(31,32,34,0) 75%);
  }
  .front__brand {
    position: absolute; left: 0; right: 0; top: 185px;
    display: flex; justify-content: center; align-items: center; gap: 18px;
  }
  .brand-name {
    font-family: "Roboto", Arial, sans-serif;
    font-weight: 700; color: var(--brand-blue);
    letter-spacing: -1px;
  }
  .front .brand-name { font-size: 78px; }
  .brand-dot { border-radius: 50%; background: var(--brand-blue); }
  .front .brand-dot { width: 22px; height: 22px; }
  .front__url {
    position: absolute; left: 0; right: 0; top: 305px;
    text-align: center; color: var(--text-light);
    font-size: 17px; letter-spacing: 9px;
  }

  /* Back */
  .back__brand {
    position: absolute; left: 80px; top: 120px;
    display: flex; align-items: center; gap: 12px;
  }
  .back .brand-name { font-size: 50px; }
  .back .brand-dot { width: 14px; height: 14px; }
  .back__accent {
    position: absolute; left: 420px; top: 110px; width: 4px; height: 55px; background: var(--cyan);
  }
  .back__divider {
    position: absolute; left: 420px; top: 190px; width: 3px; height: 180px; background: var(--divider);
  }
  .person { position: absolute; left: 455px; top: 108px; }
  .person__name { color: var(--cyan); font-size: 38px; font-weight: 400; }
  .person__role { color: var(--text-light); font-size: 19px; margin-top: 4px; }
  .contacts { position: absolute; left: 455px; top: 230px; list-style: none; }
  .contacts__item {
    display: flex; align-items: center; gap: 16px;
    color: var(--text-muted); font-size: 18px; letter-spacing: 1px;
    height: 44px;
  }
  .contacts__icon { width: 26px; height: 26px; flex: none; }
  .edge-band { position: absolute; bottom: 0; height: 16px; background: var(--cyan); }
  .edge-band--a { left: 0; width: 220px; }
  .edge-band--b { left: 232px; width: 110px; }
  .edge-band--c { left: 354px; right: 0; }
</style>
</head>
<body>
<main class="sheet">

  <section class="card front">
    <div class="front__map" role="img" aria-label="Faint world map spanning the card background"></div>
    <div class="front__brand">
      <span class="brand-name">BrivoMatex</span>
      <span class="brand-dot"></span>
    </div>
    <p class="front__url">www.brivomatex.example</p>
  </section>

  <section class="card back">
    <div class="back__brand">
      <span class="brand-name">BrivoMatex</span>
      <span class="brand-dot"></span>
    </div>
    <span class="back__accent"></span>
    <span class="back__divider"></span>
    <div class="person">
      <h1 class="person__name">Tommaso Ferlini</h1>
      <p class="person__role">CEO &amp; Founder</p>
    </div>
    <ul class="contacts">
      <li class="contacts__item">
        <svg class="contacts__icon" viewBox="0 0 26 26" aria-hidden="true">
          <circle cx="13" cy="13" r="13" fill="var(--cyan)"/>
          <path d="M9 7.5c.6-.4 1.3-.3 1.7.3l1.2 1.9c.3.5.2 1.1-.2 1.5l-.8.7c.7 1.5 1.7 2.6 3.2 3.3l.7-.8c.4-.4 1-.5 1.5-.2l1.9 1.2c.6.4.7 1.1.3 1.7l-.8 1c-.6.7-1.6.9-2.5.5-3.4-1.5-5.8-3.9-7.2-7.3-.4-.9-.2-1.9.5-2.5z" fill="#161719"/>
        </svg>
        +34 611.205.938
      </li>
      <li class="contacts__item">
        <svg class="contacts__icon" viewBox="0 0 26 26" aria-hidden="true">
          <circle cx="13" cy="13" r="13" fill="var(--cyan)"/>
          <rect x="7" y="8.5" width="12" height="9" rx="1" fill="none" stroke="#161719" stroke-width="1.6"/>
          <path d="M7.5 9.5l5.5 4.2 5.5-4.2" fill="none" stroke="#161719" stroke-width="1.6"/>
        </svg>
        tommaso.ferlini@brivomatex.example
      </li>
      <li class="contacts__item">
        <svg class="contacts__icon" viewBox="0 0 26 26" aria-hidden="true">
          <circle cx="13" cy="13" r="13" fill="var(--cyan)"/>
          <g fill="none" stroke="#161719" stroke-width="1.4">
            <circle cx="13" cy="13" r="6.5"/>
            <ellipse cx="13" cy="13" rx="3" ry="6.5"/>
            <path d="M6.5 13h13M7.5 9.8h11M7.5 16.2h11"/>
          </g>
        </svg>
        www.brivomatex.example
      </li>
    </ul>
    <span class="edge-band edge-band--a"></span>
    <span class="edge-band edge-band--b"></span>
    <span class="edge-band edge-band--c"></span>
  </section>

</main>
</body>
</html>
```